Invitation to Retail Shopping Event

-Must include logo
-Can contain product pictures depending on design
-I prefer any graphics to be my own product pictures
-Should include the following language:
Sip and Shop
Thursday, November 18
11 to 1 pm
478 Fenwick Lane
Come enjoy sips, snacks and shopping! Be the first to preview our new winter collection and get an early start on your holiday gifting.
Please RSVP to 402-319-5577 or info@pelbrika.com

```html
<!DOCTYPE html>
<html lang="en">
<head>
<meta charset="utf-8">
<title>Pelbrika – Sip &amp; Shop Invitation</title>
<link rel="stylesheet" href="https://fonts.googleapis.com/css2?family=Parisienne&family=Didact+Gothic&family=Montserrat:wght@500&display=swap">
<style>
  :root {
    --night: #000000;
    --copper-edge: #b57a4c;
    --gold-deep: #dcae4a;
    --gold-light: #fbf08f;
    --paper: #fdfdfc;
    --brown: #8a3f26;
    --pill: #ad6647;
    --ornament-gold: #e0b257;
  }
  * { box-sizing: border-box; margin: 0; padding: 0; }
  html, body { width: 1200px; height: 1200px; overflow: hidden; background: var(--night); }
  .canvas { position: relative; width: 1200px; height: 1200px; background: var(--night); font-family: "Didact Gothic", sans-serif; color: var(--brown); }
  .gold-frame {
    position: absolute; left: 222px; top: 0; width: 756px; height: 1200px;
    background: linear-gradient(180deg, var(--gold-deep) 0%, var(--gold-light) 50%, var(--gold-deep) 100%);
    border-left: 9px solid var(--copper-edge); border-right: 9px solid var(--copper-edge);
  }
  .invitation-panel {
    position: absolute; left: 269px; top: 0; width: 661px; height: 1200px;
    background: var(--paper); box-shadow: 0 0 10px rgba(120, 80, 20, 0.35);
  }
  .centered { position: absolute; left: 0; width: 1200px; text-align: center; }
  .brand-name { top: 76px; font-size: 52px; letter-spacing: 3px; line-height: 1; }
  .event-title { top: 200px; font-family: "Parisienne", cursive; font-size: 104px; line-height: 1; }
  .date-row { position: absolute; top: 360px; left: 0; width: 1200px; height: 60px; }
  .date-month { position: absolute; left: 436px; top: 22px; font-size: 21px; }
  .date-day { position: absolute; left: 560px; width: 104px; top: 2px; text-align: center; font-size: 22px; line-height: 1.1; }
  .date-day span { display: block; font-size: 38px; }
  .date-year { position: absolute; left: 716px; top: 20px; font-size: 23px; }
  .date-rule { position: absolute; top: 16px; width: 2px; height: 38px; background: var(--brown); }
  .event-time {
    position: absolute; left: 506px; top: 462px; width: 188px; height: 45px;
    background: var(--pill); color: #fff; border-radius: 22px 0 22px 0;
    font-family: "Montserrat", sans-serif; font-weight: 500; font-size: 24px; letter-spacing: 3px;
    display: flex; align-items: center; justify-content: center;
  }
  .venue { top: 554px; font-size: 26px; }
  .tagline { top: 626px; font-size: 31px; line-height: 39px; }
  .divider { position: absolute; left: 480px; top: 728px; }
  .details { top: 786px; font-size: 24px; line-height: 30px; letter-spacing: 0.3px; }
  .rsvp { top: 892px; font-size: 24px; line-height: 32px; }
  .rsvp .contact { display: block; }
  .rsvp .phone { font-size: 27px; }
  .rsvp .joiner { margin-top: 2px; }
  .rsvp .email { margin-top: 14px; }
  .ornament, .product-photo { position: absolute; }
  .ornament { background: radial-gradient(circle at center, var(--ornament-gold) 0%, rgba(224,178,87,0.35) 70%, rgba(224,178,87,0) 100%); }
  .mandala-left { left: 269px; top: 428px; width: 105px; height: 212px; border-radius: 0 106px 106px 0; }
  .mandala-right { left: 820px; top: 428px; width: 110px; height: 212px; border-radius: 106px 0 0 106px; }
  .product-photo { width: 124px; height: 120px; border-radius: 50%; background: radial-gradient(circle, #e9e3d6 0%, #e6bd55 40%, rgba(230,189,85,0.15) 75%, rgba(255,255,255,0) 100%); }
  .earring-left { left: 312px; top: 920px; }
  .earring-right { left: 760px; top: 920px; }
  .flourish { position: absolute; left: 392px; top: 1098px; width: 416px; height: 36px;
    background: linear-gradient(90deg, rgba(138,63,38,0) 0%, rgba(138,63,38,0.5) 35%, rgba(138,63,38,0.7) 50%, rgba(138,63,38,0.5) 65%, rgba(138,63,38,0) 100%); border-radius: 18px; }
</style>
</head>
<body>
<main class="canvas">
  <div class="gold-frame"></div>
  <section class="invitation-panel"></section>

  <div class="ornament mandala-left" role="img" aria-label="Gold lace mandala ornament"></div>
  <div class="ornament mandala-right" role="img" aria-label="Gold lace mandala ornament"></div>

  <h1 class="centered brand-name">PELBRIKA</h1>
  <h2 class="centered event-title">Sip &amp; Shop</h2>

  <div class="date-row">
    <span class="date-month">November</span>
    <span class="date-rule" style="left:548px"></span>
    <span class="date-day">Thursday<span>18</span></span>
    <span class="date-rule" style="left:687px"></span>
    <span class="date-year">2021</span>
  </div>

  <div class="event-time">11 to 1 pm</div>
  <p class="centered venue">478 Fenwick Lane</p>
  <p class="centered tagline">Come enjoy sips,<br>snacks and shopping !</p>

  <svg class="divider" width="240" height="16" viewBox="0 0 240 16" aria-hidden="true">
    <path d="M0 8 Q60 6 112 5 L112 11 Q60 10 0 8 Z" fill="var(--brown)"/>
    <path d="M240 8 Q180 6 146 5 L146 11 Q180 10 240 8 Z" fill="var(--brown)"/>
    <circle cx="104" cy="8" r="3" fill="var(--brown)"/>
    <rect x="117" y="5" width="6" height="6" transform="rotate(45 120 8)" fill="var(--brown)"/>
    <circle cx="136" cy="8" r="3" fill="var(--brown)"/>
  </svg>

  <p class="centered details">Be the first to preview our new winter collection<br>and get an early start on your holiday gifting.</p>

  <div class="product-photo earring-left" role="img" aria-label="Gold quatrefoil earring with diamonds"></div>
  <div class="product-photo earring-right" role="img" aria-label="Gold quatrefoil earring with diamonds"></div>

  <p class="centered rsvp">
    <span class="contact">Please RSVP to</span>
    <span class="contact phone">402-319-5577</span>
    <span class="contact joiner">or</span>
    <span class="contact email">info@pelbrika.com</span>
  </p>

  <div class="flourish" role="img" aria-label="Decorative scroll flourish divider"></div>
</main>
</body>
</html>
```